Professional, Attractive, Simple Website Needed!!

We completed the design for our logo.

We need a website built out around this.

Here are a couple samples of how we want ours formatted.

http://brvntapower.com

http://www.halvorbeam.com/lp/free-quote?LeadSource=Search%20Engine&ProgramName=webquery&experience=qual&language=en&type=brd&gclid=Xq7RTPwmEYKDLAvUHbsNQkfPZrTcGwnJuoVbXeLqHmRYdAsWtPkMcNfBYgzTrUoQJhEdWvKpYaLsZbCmNDgQwTxAoKpXbT_qkR

http://morvalo.co

Reason: Extending this deadline due to our delay in providing designers with content for each page. This is coming in next 24 hours.

Reason: Due to scheduling conflicts and extended travel delays related to Puerto Rico, the deadline has been extended. Your patience is greatly appreciated.

Reason: Travel and scheduling conflicts have made it impossible to give this project the thorough review it deserves, therefore I am extending the deadline. Thank you for your patience!

Target Market(s)

Home Owners who earn 60k + household annually

Industry/Entity Type

It Professional

Coding

Coded - Design and coding required

Number of Pages Required

5+ page

Font styles to use
Serif

Colors
34a7d8
9bcb3c

Requirements
Must have
• Simple
• Lead form Entry (Ability for visitor to enter Name, number and address for a quote)
• Sleek Design
• Professional
• Testimonials
• Use color Scheme of Design Logo Attached
Nice to have
• Video when site starts
• Like this
• https://www.vidmarrow.com/watch?v=qT8mRpXw2Ka&feature=vidm.ro
Should not have
• Should not include Commercial solar
• Should not include wind power

```html
<!DOCTYPE html>
<html lang="en">
<head>
<meta charset="utf-8">
<title>Brightfield Power – The Solar Services</title>
<link href="https://fonts.googleapis.com/css2?family=Fjalla+One&family=Open+Sans:wght@400;600;700&display=swap" rel="stylesheet">
<style>
:root{
  --ink:#2b2f36;
  --muted:#8a8f96;
  --green:#9bcb3c;
  --blue:#34a7d8;
  --band-blue:#0b8ecf;
  --cta-blue:#06a6ee;
  --step-blue:#1ea1e0;
  --soft-gray:#f3f3f3;
  --footer:#333a44;
  --white:#ffffff;
}
*{margin:0;padding:0;box-sizing:border-box}
html,body{width:757px;height:1200px;overflow:hidden}
body{position:relative;font-family:"Open Sans",sans-serif;color:var(--ink);background:var(--white)}
.abs{position:absolute}
.center{left:0;width:757px;text-align:center}
.display{font-family:"Fjalla One",sans-serif;text-transform:uppercase}

/* hero */
.hero{top:0;left:0;width:757px;height:358px;overflow:hidden}
.hero-photo{position:absolute;inset:0;background:
  radial-gradient(ellipse 260px 120px at 300px 330px,rgba(170,110,60,.55),transparent 70%),
  linear-gradient(160deg,#3a4048 0%,#2a3038 45%,#20252c 75%,#3b3530 100%)}
.brand{top:34px;display:flex;justify-content:center;align-items:center;gap:8px}
.brand-dot{width:14px;height:14px;border-radius:50%;background:var(--green)}
.brand-name{font-weight:600;font-size:20px;color:var(--blue);letter-spacing:.5px}
.menu{top:43px;left:646px;width:16px;height:11px}
.menu span{display:block;height:2px;background:var(--white);margin-bottom:2.5px}
.hero-title{top:151px;font-size:22px;color:var(--white)}
.hero-lead{top:183px;font-size:10px;line-height:12px;color:#e6e8ea;letter-spacing:.3px}
.form-label{top:261px;font-size:9.5px;font-weight:700;letter-spacing:1px;color:var(--white)}
.quote-form{top:280px;left:202px;width:351px;height:29px;display:flex}
.zip{width:200px;height:29px;background:var(--white);color:#b9bcc0;font-size:10px;line-height:29px;padding-left:10px}
.next{flex:1;background:var(--green);color:var(--white);font-weight:700;font-size:11px;text-align:center;line-height:29px}

/* savings band */
.savings{top:358px;left:0;width:757px;height:127px;background:var(--band-blue);color:var(--white)}
.eyebrow{font-size:10.5px;letter-spacing:.3px}
.dots{display:flex;justify-content:center;gap:4px}
.dots i{width:4px;height:4px;border-radius:50%;background:currentColor}
.savings-headline{font-size:25px}

/* steps */
.steps-title{top:519px;font-size:10.5px;font-weight:600;color:var(--ink)}
.steps-sub{top:546px;font-size:9.5px;color:var(--muted)}
.step{width:160px;text-align:center}
.step-badge{width:94px;height:94px;border-radius:50%;background:var(--green);margin:0 auto;display:flex;align-items:center;justify-content:center}
.step-name{margin-top:12px;font-size:16px;font-weight:600;color:var(--step-blue)}
.step-text{margin-top:8px;font-size:7.5px;line-height:11px;color:#666}
.connector{top:644px}

/* testimonials */
.reviews{top:836px;left:0;width:757px;height:207px;background:var(--soft-gray)}
.reviews-title{top:864px;font-size:10.5px;font-weight:700;color:var(--ink)}
.quote-mark{font-family:Georgia,serif;font-size:64px;color:#cfcfcf;line-height:1}
.review-text{top:918px;left:148px;width:461px;text-align:center;font-size:7.6px;line-height:13.5px;color:#555}
.reviewer{top:958px;font-size:8.5px;font-weight:700;color:var(--step-blue)}
.reviewer-place{top:972px;font-size:6.5px;font-weight:700;color:var(--green)}
.nav-arrow{top:935px;font-size:14px;color:#555}

/* cta */
.cta{top:1043px;left:0;width:757px;height:110px;background:var(--cta-blue)}
.cta-text{top:1069px;left:160px;font-size:21px;line-height:28px;color:var(--white)}
.cta-button{top:1081px;left:539px;width:123px;height:35px;border:1.5px solid var(--white);color:var(--white);font-size:10.5px;letter-spacing:.4px;text-align:center;line-height:32px}

/* footer */
.footer{top:1153px;left:0;width:757px;height:47px;background:var(--footer);display:flex;justify-content:center;align-items:center;gap:7px;font-size:7px;color:#c9ccd0}
.footer i{width:3px;height:3px;border-radius:50%;background:var(--green)}
</style>
</head>
<body>

<header class="hero abs">
  <div class="hero-photo" role="img" aria-label="Photo of solar panels at dusk under a cloudy sky"></div>
</header>
<div class="brand abs center"><span class="brand-dot"></span><span class="brand-name">BRIGHTFIELD POWER</span></div>
<div class="menu abs" aria-label="Menu"><span></span><span></span><span></span></div>
<h1 class="hero-title abs center display">The Solar Services</h1>
<p class="hero-lead abs center">Our energy services are know be one of the most reliable affordable,<br>because we take pride in delivering the best</p>
<p class="form-label abs center">ENTER YOUR DETAILS TO CALCULATE YOUR SAVINGS</p>
<div class="quote-form abs"><div class="zip">Your Zip Code</div><div class="next">NEXT</div></div>

<section class="savings abs">
  <p class="eyebrow abs center" style="top:28px">BRIGHTFIELD POWER</p>
  <div class="dots abs center" style="top:52px"><i></i><i></i><i></i></div>
  <h2 class="savings-headline abs center display" style="top:68px">Go Solar and Save 20% on Your Electric Bill*</h2>
</section>

<h3 class="steps-title abs center">HOW IT WORKS</h3>
<div class="dots abs center" style="top:536px;color:var(--green)"><i></i><i></i><i></i></div>
<p class="steps-sub abs center">THREE EASY STEPS TO GOING SOLAR</p>

<div class="step abs" style="left:109px;top:595px">
  <div class="step-badge">
    <svg width="62" height="52" viewBox="0 0 62 52" fill="none" stroke="#fff" stroke-width="2"><rect x="1" y="1" width="60" height="50"/><line x1="1" y1="10" x2="61" y2="10"/><circle cx="6" cy="5.5" r="1"/><circle cx="11" cy="5.5" r="1"/><line x1="20" y1="16" x2="20" y2="46"/><line x1="40" y1="16" x2="40" y2="46"/><line x1="8" y1="24" x2="16" y2="24"/><line x1="8" y1="32" x2="14" y2="32"/><line x1="46" y1="32" x2="54" y2="32"/></svg>
  </div>
  <p class="step-name">Step 1</p>
  <p class="step-text">We'll design your<br>solar panel system</p>
</div>
<div class="step abs" style="left:298px;top:595px">
  <div class="step-badge">
    <svg width="62" height="52" viewBox="0 0 62 52" fill="none" stroke="#fff" stroke-width="2"><rect x="1" y="6" width="60" height="45" rx="5"/><g stroke-width="1.6"><line x1="10" y1="1" x2="10" y2="9"/><line x1="20" y1="1" x2="20" y2="9"/><line x1="31" y1="1" x2="31" y2="9"/><line x1="42" y1="1" x2="42" y2="9"/><line x1="52" y1="1" x2="52" y2="9"/></g><g stroke-width="1.6"><rect x="8" y="16" width="8" height="7"/><rect x="20" y="16" width="8" height="7"/><rect x="32" y="16" width="8" height="7"/><rect x="44" y="16" width="8" height="7"/><rect x="8" y="27" width="8" height="7"/><rect x="20" y="27" width="8" height="7"/><rect x="32" y="27" width="8" height="7"/><rect x="44" y="27" width="8" height="7"/><rect x="8" y="38" width="8" height="7"/><rect x="20" y="38" width="8" height="7"/><rect x="32" y="38" width="8" height="7"/><rect x="44" y="38" width="8" height="7"/></g></svg>
  </div>
  <p class="step-name">Step 2</p>
  <p class="step-text">Schedule your<br>1 day install</p>
</div>
<div class="step abs" style="left:487px;top:595px">
  <div class="step-badge">
    <svg width="60" height="56" viewBox="0 0 60 56" fill="none" stroke="#fff" stroke-width="2"><circle cx="30" cy="8" r="7"/><text x="30" y="12" fill="#fff" stroke="none" font-size="10" font-family="Open Sans,sans-serif" text-anchor="middle">$</text><ellipse cx="30" cy="33" rx="22" ry="14"/><line x1="20" y1="45" x2="20" y2="54"/><line x1="40" y1="45" x2="40" y2="54"/><path d="M52 30h5v7h-5"/><circle cx="44" cy="28" r="1"/></svg>
  </div>
  <p class="step-name">Step 3</p>
  <p class="step-text">Start saving on your<br>electricity bill</p>
</div>

<svg class="connector abs" style="left:244px" width="80" height="8" viewBox="0 0 80 8"><line x1="0" y1="4" x2="74" y2="4" stroke="#1ea1e0" stroke-width="1" stroke-dasharray="2 2"/><path d="M74 0l6 4-6 4z" fill="#1ea1e0"/></svg>
<svg class="connector abs" style="left:433px" width="80" height="8" viewBox="0 0 80 8"><line x1="0" y1="4" x2="74" y2="4" stroke="#1ea1e0" stroke-width="1" stroke-dasharray="2 2"/><path d="M74 0l6 4-6 4z" fill="#1ea1e0"/></svg>

<section class="reviews abs"></section>
<h3 class="reviews-title abs center">WHAT OUR CLIENT SAY ABOUT US</h3>
<div class="dots abs center" style="top:883px;color:var(--green)"><i></i><i></i><i></i></div>
<span class="quote-mark abs" style="left:138px;top:870px">&ldquo;</span>
<span class="quote-mark abs" style="left:617px;top:962px">&rdquo;</span>
<span class="nav-arrow abs" style="left:98px">&#8249;</span>
<span class="nav-arrow abs" style="left:656px">&#8250;</span>
<p class="review-text abs">Customer service from Marcus and the overall functionality of the PV arrays have exceeded my expectations. Who knew making the switch to solar could be so easy, awesome, and rewarding?!</p>
<p class="reviewer abs center">Derek Holloway</p>
<p class="reviewer-place abs center">Elmford, MA</p>

<section class="cta abs"></section>
<h2 class="cta-text abs display">Ready to join the world's<br>fastest growing solar company ?</h2>
<div class="cta-button abs">CONTACT NOW</div>

<footer class="footer abs">
  <span>Home</span><i></i><span>About</span><i></i><span>Products</span><i></i><span>Testimonials</span><i></i><span>Contact us</span>
</footer>

</body>
</html>
```